R&T Architects - business card and stationary

Aloha,

We have a simple text logo, we need it incorporated into a business card and also stationary design (letterhead) if possible.

Please check out our website, rtmpacific.com for a little more about us. The logo we would like to use is in the upper left corner of the website. It is a simple colored logo based on the Klavica font. We are open to new logo's as well, but we want simple.

Thanks

```html
<!DOCTYPE html>
<html lang="en">
<head>
<meta charset="utf-8">
<title>R&amp;T Architects – Stationery</title>
<link rel="stylesheet" href="https://fonts.googleapis.com/css2?family=Ubuntu:wght@400;500&display=swap">
<style>
  :root {
    --backdrop: #58585a;
    --paper: #ffffff;
    --bronze: #7f6a1a;
    --leaf: #7b9a2c;
    --font: "Ubuntu", sans-serif;
  }
  html, body {
    margin: 0;
    padding: 0;
    overflow: hidden;
  }
  body {
    width: 1200px;
    height: 1150px;
    background: var(--backdrop);
    font-family: var(--font);
    position: relative;
  }
  .sheet {
    position: absolute;
    background: var(--paper);
  }
  .band {
    position: absolute;
    height: 100%;
    top: 0;
  }
  .band--bronze { background: var(--bronze); }
  .band--leaf { background: var(--leaf); }
  .stripe {
    position: absolute;
    left: 0;
    width: 100%;
  }
  .company-name {
    font-weight: 500;
    color: var(--bronze);
    margin: 0;
    white-space: nowrap;
  }

  /* Card front */
  .card-front { left: 24px; top: 28px; width: 316px; height: 182px; }
  .card-front .stripe { height: 10px; }
  .card-front .stripe--top { top: 0; }
  .card-front .stripe--bottom { bottom: 0; }
  .card-front .company-name {
    position: absolute;
    left: 0; right: 0;
    top: 74px;
    text-align: center;
    font-size: 32px;
  }

  /* Card back */
  .card-back { left: 24px; top: 234px; width: 316px; height: 180px; }
  .card-back .stripe { height: 10px; }
  .card-back .stripe--top { top: 0; }
  .card-back .stripe--bottom { bottom: 0; }
  .card-back .company-name {
    position: absolute;
    left: 20px;
    top: 32px;
    font-size: 22px;
  }
  .contact {
    position: absolute;
    font-size: 10px;
    line-height: 13px;
    color: var(--bronze);
    margin: 0;
    white-space: nowrap;
  }
  .contact--person { left: 14px; top: 96px; }
  .contact--email { left: 142px; top: 109px; color: var(--leaf); }
  .contact--postal { left: 14px; top: 136px; }
  .contact--street { left: 158px; top: 136px; }
  .contact .label { text-transform: uppercase; }

  /* Letterhead */
  .letterhead { left: 372px; top: 28px; width: 738px; height: 1042px; }
  .letterhead .stripe { height: 16px; }
  .letterhead .stripe--top { top: 0; }
  .letterhead .stripe--bottom { bottom: 0; }
  .letterhead .company-name {
    position: absolute;
    left: 0; right: 0;
    top: 50px;
    text-align: center;
    font-size: 32px;
  }
  .letterhead-address {
    position: absolute;
    font-size: 10px;
    line-height: 13px;
    color: var(--bronze);
    margin: 0;
    top: 986px;
    white-space: nowrap;
  }
  .letterhead-address--postal { left: 248px; }
  .letterhead-address--street { left: 376px; color: var(--leaf); }
</style>
</head>
<body>

  <section class="sheet card-front" aria-label="Business card front">
    <div class="stripe stripe--top">
      <span class="band band--bronze" style="left:0;width:200px"></span>
      <span class="band band--leaf" style="left:208px;width:108px"></span>
    </div>
    <h1 class="company-name">R&amp;T Architects</h1>
    <div class="stripe stripe--bottom">
      <span class="band band--bronze" style="left:0;width:196px"></span>
      <span class="band band--leaf" style="left:204px;width:112px"></span>
    </div>
  </section>

  <section class="sheet card-back" aria-label="Business card back">
    <div class="stripe stripe--top">
      <span class="band band--bronze" style="left:0;width:200px"></span>
      <span class="band band--leaf" style="left:208px;width:108px"></span>
    </div>
    <h2 class="company-name">R&amp;T Architects</h2>
    <p class="contact contact--person"><span class="label">Dana Miyake</span><br>(808) 555-0142</p>
    <p class="contact contact--email">dana@rtmpacific.com</p>
    <p class="contact contact--postal">P.A: 12-3456 Kealoha Place<br>Pualani Bay, Hawaii 96799</p>
    <p class="contact contact--street">A: 12-3478 Makai Road<br>Pualani Bay, Hawaii 96799</p>
    <div class="stripe stripe--bottom">
      <span class="band band--bronze" style="left:0;width:196px"></span>
      <span class="band band--leaf" style="left:204px;width:112px"></span>
    </div>
  </section>

  <section class="sheet letterhead" aria-label="Letterhead">
    <div class="stripe stripe--top">
      <span class="band band--bronze" style="left:0;width:464px"></span>
      <span class="band band--leaf" style="left:484px;width:254px"></span>
    </div>
    <h2 class="company-name">R&amp;T Architects</h2>
    <p class="letterhead-address letterhead-address--postal">P.A: 12-3456 Kealoha Place<br>Pualani Bay, Hawaii 96799</p>
    <p class="letterhead-address letterhead-address--street">A: 12-3478 Makai Road Pualani Bay,<br>Hawaii 96799</p>
    <div class="stripe stripe--bottom">
      <span class="band band--bronze" style="left:0;width:464px"></span>
      <span class="band band--leaf" style="left:484px;width:254px"></span>
    </div>
  </section>

</body>
</html>
```